Brightwave Reach - Business Card

We need a business card for a Social Media Marketing company that specializes in online marketing for small businesses in Canada using common Social Media platforms such as Pictora, Kinloop, Blinkit & Chirpo.

I have uploaded a copy of our logo which I would like utilized in the business card. We would like the business card to be modern yet classy design.

Our website is www.brightwavereach.ca

Industry/Entity Type

Marketing

Contact Information for Business Card

Email: info@brightwavereach.ca
Website: www.brightwavereach.ca
Telephone: 604-392-5108

Colors

Designer to choose colors to be used in the design.

Requirements
Must have
• Social Media icons on reverse
• Please add some designs with color.

```html
<!DOCTYPE html>
<html lang="en">
<head>
<meta charset="utf-8">
<title>Brightwave Reach – Business Card</title>
<link rel="stylesheet" href="https://fonts.googleapis.com/css2?family=Questrial&display=swap">
<style>
  :root {
    --canvas: #ffffff;
    --front-bg: #ffffff;
    --front-edge: #d9d9d9;
    --ink: #4a4d50;
    --faint-light: #ececec;
    --back-bg: #3f4245;
    --faint-dark: #36393c;
    --back-text: #e4e5e6;
    --tab-bg: #cfcfcf;
    --tab-bg-dark: #5a5d60;
    --chip: #3f4245;
    --chip-text: #ffffff;
  }
  * { margin: 0; padding: 0; box-sizing: border-box; }
  html, body {
    width: 1200px; height: 388px; overflow: hidden;
    background: var(--canvas);
    font-family: "Questrial", "Century Gothic", sans-serif;
  }
  .card {
    position: absolute; top: 33px;
    width: 535px; height: 297px; overflow: hidden;
  }
  .card--front { left: 29px; background: var(--front-bg); border: 1px solid var(--front-edge); }
  .card--back { left: 610px; background: var(--back-bg); }

  .texture {
    position: absolute; inset: 0;
  }
  .card--front .texture {
    background:
      linear-gradient(135deg, transparent 8%, var(--faint-light) 8%, var(--faint-light) 20%, transparent 20%,
        transparent 36%, var(--faint-light) 36%, var(--faint-light) 50%, transparent 50%,
        transparent 66%, var(--faint-light) 66%, var(--faint-light) 78%, transparent 78%);
  }
  .card--back .texture {
    background:
      linear-gradient(135deg, transparent 8%, var(--faint-dark) 8%, var(--faint-dark) 20%, transparent 20%,
        transparent 36%, var(--faint-dark) 36%, var(--faint-dark) 50%, transparent 50%,
        transparent 66%, var(--faint-dark) 66%, var(--faint-dark) 78%, transparent 78%);
  }

  .brand {
    position: absolute; left: 0; top: 0; width: 535px; height: 297px;
    display: flex; flex-direction: column; align-items: center; justify-content: center;
    color: var(--ink);
  }
  .brand__name {
    font-size: 46px; line-height: 1.05; text-transform: uppercase;
    text-align: center; letter-spacing: 1px;
  }
  .brand__mark {
    width: 16px; height: 16px; margin-top: 18px; background: var(--ink);
  }

  .contact {
    position: absolute; left: 0; top: 124px; width: 535px;
    text-align: center; color: var(--back-text);
    font-size: 13.5px; line-height: 17.5px;
    list-style: none;
  }

  .social-tab {
    position: absolute; right: 0; top: 78px;
    width: 32px; height: 148px;
    display: flex; flex-direction: column; align-items: center; justify-content: space-around;
    padding: 4px 0;
    list-style: none;
  }
  .card--front .social-tab { background: var(--tab-bg); }
  .card--back .social-tab { background: var(--tab-bg-dark); }
  .social-tab__item {
    display: flex; flex-direction: column; align-items: center;
    font-size: 6px; line-height: 7px; color: var(--chip);
  }
  .card--back .social-tab__item { color: var(--chip-text); }
  .social-tab__chip {
    width: 17px; height: 17px; border-radius: 4px; background: var(--chip); margin-bottom: 2px;
  }
  .card--back .social-tab__chip { background: #2f3134; }
</style>
</head>
<body>

<section class="card card--front">
  <div class="texture" role="img" aria-label="Faint large diagonal brand lettering in the background"></div>
  <div class="brand">
    <div class="brand__name">Brightwave<br>Reach</div>
    <div class="brand__mark"></div>
  </div>
  <ul class="social-tab">
    <li class="social-tab__item"><span class="social-tab__chip"></span>Circlo</li>
    <li class="social-tab__item"><span class="social-tab__chip"></span>Chirpo</li>
    <li class="social-tab__item"><span class="social-tab__chip"></span>Kinloop</li>
    <li class="social-tab__item"><span class="social-tab__chip"></span>Linkwell</li>
  </ul>
</section>

<section class="card card--back">
  <div class="texture" role="img" aria-label="Faint large diagonal brand lettering in the background"></div>
  <ul class="contact">
    <li>email: info@brightwavereach.ca</li>
    <li>website: www.brightwavereach.ca</li>
    <li>Telephone: 604-392-5108</li>
  </ul>
  <ul class="social-tab">
    <li class="social-tab__item"><span class="social-tab__chip"></span>Circlo</li>
    <li class="social-tab__item"><span class="social-tab__chip"></span>Chirpo</li>
    <li class="social-tab__item"><span class="social-tab__chip"></span>Kinloop</li>
    <li class="social-tab__item"><span class="social-tab__chip"></span>Linkwell</li>
  </ul>
</section>

</body>
</html>
```